Lucky Velvet Game Evenings Business Card Design

I need a business card for a fun casino entertainment business. I would like one side of the business card to convey the feel of a playing card similar to the playing card uploaded but with one logo placed horizontally across the card and the web address below it.
the information side can be slightly more plain, maybe just a stack of chips along one side or something with a casino feel.

Industry/Entity Type

Casino

Contact Information for Business Card

Lucky Velvet Game Evenings
Ted Morrowick
Director
0438 216590
ted@luckyvelvetparties.com.au

```html
<!DOCTYPE html>
<html lang="en">
<head>
<meta charset="utf-8">
<title>Lucky Velvet Game Evenings – Business Cards</title>
<link rel="stylesheet" href="https://fonts.googleapis.com/css2?family=Quicksand:wght@500;700&family=Cabin:wght@500&display=swap">
<style>
:root{
  --page:#ffffff;
  --card-black:#050505;
  --card-glow:#3a3a3a;
  --pattern-grey:#5a5a5a;
  --gold-light:#fbe98c;
  --gold:#f2b418;
  --orange:#d9641c;
  --ink-dark:#1a1208;
  --text-white:#ffffff;
  --text-soft:#e8e8e8;
}
*{margin:0;padding:0;box-sizing:border-box}
html,body{width:1200px;height:1000px;overflow:hidden;background:var(--page)}
body{position:relative;font-family:"Quicksand",sans-serif;color:var(--text-white)}
.card{position:absolute;border-radius:24px;overflow:hidden;background:var(--card-black)}
.card--front-top{left:5px;top:130px;width:583px;height:337px}
.card--back-top{left:612px;top:130px;width:585px;height:340px}
.card--front-bottom{left:5px;top:537px;width:583px;height:338px}
.card--back-bottom{left:607px;top:537px;width:588px;height:340px}

.suit-field{position:absolute;inset:0;
  background:radial-gradient(ellipse 55% 60% at 50% 45%,var(--card-glow) 0%,#151515 60%,var(--card-black) 100%)}
.suit-field--strong{background:radial-gradient(ellipse 70% 80% at 50% 50%,#6a6a6a 0%,#3c3c3c 55%,#1e1e1e 100%)}

.brand-name{position:absolute;left:0;right:0;top:128px;text-align:center;
  font-weight:700;font-size:40px;line-height:1.1;color:var(--gold);padding:0 60px}
.web-band{position:absolute;left:0;right:0;bottom:0;height:35px;
  background:linear-gradient(90deg,var(--gold) 0%,var(--orange) 25%,var(--gold) 60%,var(--gold-light) 100%);
  display:flex;align-items:center;justify-content:center;
  font-family:"Cabin",sans-serif;font-weight:500;font-size:22px;color:var(--ink-dark)}

.back-title{position:absolute;left:0;right:0;top:108px;text-align:center;font-weight:700;font-size:24px;letter-spacing:.3px}
.orange-rule{position:absolute;left:0;right:0;top:180px;height:7px;
  background:linear-gradient(90deg,var(--orange) 0%,var(--gold) 45%,var(--orange) 100%)}
.person{position:absolute;left:24px;top:256px}
.person__name{font-weight:700;font-size:21px}
.person__role{font-weight:700;font-size:19px;margin-top:10px;margin-left:4px}
.contact{position:absolute;right:22px;top:270px;text-align:right;font-weight:500;font-size:17px;color:var(--text-soft);line-height:1.65}
.contact svg{vertical-align:-2px;margin-left:5px}

.title-bar{position:absolute;left:0;right:0;top:156px;display:flex;align-items:center;gap:10px}
.title-bar__bar{flex:1;height:22px;background:linear-gradient(90deg,var(--orange),var(--gold) 60%,var(--orange))}
.title-bar__text{font-weight:700;font-size:22px;white-space:nowrap}
.stack{position:absolute;left:0;right:0;top:208px;text-align:center}
.stack__name{font-weight:700;font-size:21px}
.stack__role{font-weight:500;font-size:19px;margin-top:8px;color:var(--text-soft)}
.stack__line{font-weight:500;font-size:16px;margin-top:4px;color:var(--text-soft)}
.stack__line svg{vertical-align:-2px;margin-right:5px}
</style>
</head>
<body>

<section class="card card--front-top">
  <div class="suit-field" role="img" aria-label="Faint repeating pattern of card suits on black"></div>
  <div class="brand-name">Lucky Velvet Game Evenings</div>
  <div class="web-band">www.luckyvelvetparties.com.au</div>
</section>

<section class="card card--back-top">
  <div class="suit-field" role="img" aria-label="Faint repeating pattern of card suits on black"></div>
  <div class="back-title">LUCKY VELVET GAME EVENINGS</div>
  <div class="orange-rule"></div>
  <div class="person">
    <div class="person__name">TED MORROWICK</div>
    <div class="person__role">Director</div>
  </div>
  <div class="contact">
    <div>0438 216590<svg width="10" height="15" viewBox="0 0 10 15"><rect x="1" y="1" width="8" height="13" rx="1.5" fill="none" stroke="#fff" stroke-width="1.5"/><rect x="4" y="11" width="2" height="1.5" fill="#fff"/></svg></div>
    <div>ted@luckyvelvetparties.com.au<svg width="13" height="10" viewBox="0 0 13 10"><rect x=".75" y=".75" width="11.5" height="8.5" fill="none" stroke="#fff" stroke-width="1.5"/><path d="M1 1l5.5 4.5L12 1" fill="none" stroke="#fff" stroke-width="1.3"/></svg></div>
  </div>
</section>

<section class="card card--front-bottom">
  <div class="suit-field" role="img" aria-label="Faint repeating pattern of card suits on black"></div>
  <div class="brand-name">Lucky Velvet Game Evenings</div>
  <div class="web-band">www.luckyvelvetparties.com.au</div>
</section>

<section class="card card--back-bottom">
  <div class="suit-field suit-field--strong" role="img" aria-label="Repeating grey pattern of hearts, clubs, diamonds and spades"></div>
  <div class="title-bar">
    <span class="title-bar__bar"></span>
    <span class="title-bar__text">LUCKY VELVET GAME EVENINGS</span>
    <span class="title-bar__bar"></span>
  </div>
  <div class="stack">
    <div class="stack__name">TED MORROWICK</div>
    <div class="stack__role">Director</div>
    <div class="stack__line"><svg width="10" height="15" viewBox="0 0 10 15"><rect x="1" y="1" width="8" height="13" rx="1.5" fill="none" stroke="#fff" stroke-width="1.5"/><rect x="4" y="11" width="2" height="1.5" fill="#fff"/></svg>0438 216590</div>
    <div class="stack__line"><svg width="13" height="10" viewBox="0 0 13 10"><rect x=".75" y=".75" width="11.5" height="8.5" fill="none" stroke="#fff" stroke-width="1.5"/><path d="M1 1l5.5 4.5L12 1" fill="none" stroke="#fff" stroke-width="1.3"/></svg>ted@luckyvelvetparties.com.au</div>
  </div>
</section>

</body>
</html>
```